Skip Along Today campaign: promoting kids play in the UK - Website Redesign

Skip Along Today is a national UK campaign that promotes the value of play for children. The current website is live at http://www.skipalongtoday.co.uk. This website has been live for 4 years and now needs to be redesigned. The target audience is parents of young children up to the age of 12.

The current site was designed with a series of old adverts in mind. Here is an example of an old advert: http://vidbox.example/qR7tLm2WxZa

Criticisms of existing site:
The design represented the adverts too closely. The result was a website that mirrors the adverts rather than complements them.
The color scheme is too dark.
Text-heavy pages (e.g. http://www.skipalongtoday.co.uk/fun.php) are dull and not FUN!

New site
We have recently had a series of new video adverts produced:
advert 1: http://vidbox.example/h3JkV9sNbQe
advert 2: http://vidbox.example/Wm4cPz8RtLu
advert 3: http://vidbox.example/aG5dKx1YvHo

The new site should be cleaner and brighter than the existing site, possibly with a white background using graphics, fonts and advert characters (see attached character graphics files) to add the element of fun and play.

The homepage should include:
1. Skip Along Today logo (attached)
2. Social Media links (visible on all pages of the site) – Chatterly, Peepsy, Vidbox
3. Link to the SkipAlongToday app page of the site (visible on all pages)
4. Image/video placeholder that the user can scroll through, view full-size images and play videos.
5. Text area to hold approximately 100 words describing the purpose of the campaign
6. Site footer to contain the same information as on the existing site along with the Northfield Games & Pastimes Guild logo (attached)

Site structure:
One change to the site structure… the “Brought to you by” menu item will be removed from the top-level menu.

General:
Some pages on the existing site are quite text-heavy, we would like to break up text on these pages in some way. Graphical division of paragraphs, use of advert characters?

Please note that all attached graphics file are the property of the Northfield Games & Pastimes Guild and must only be used for the purpose of this project.

```html
<!DOCTYPE html>
<html lang="en">
<head>
<meta charset="utf-8">
<title>Skip Along Today</title>
<link rel="stylesheet" href="https://fonts.googleapis.com/css2?family=Delius&family=Open+Sans:wght@400&display=swap">
<style>
  :root {
    --purple: #6a4aa3;
    --purple-dark: #553891;
    --purple-text: #6b4ea6;
    --green: #a9c93a;
    --green-dark: #93b22c;
    --ink: #2b2b2b;
    --body: #444;
    --page: #f7f7fa;
    --grid: #e6e6ee;
    --white: #ffffff;
  }
  * { box-sizing: border-box; margin: 0; padding: 0; }
  html, body { width: 1200px; height: 1130px; overflow: hidden; }
  body {
    position: relative;
    background-color: var(--page);
    background-image:
      linear-gradient(var(--grid) 1px, transparent 1px),
      linear-gradient(90deg, var(--grid) 1px, transparent 1px);
    background-size: 14px 14px;
    font-family: "Open Sans", sans-serif;
    color: var(--body);
  }
  a { color: inherit; text-decoration: none; }

  .site-logo {
    position: absolute; left: 164px; top: 48px;
    display: flex; align-items: center; gap: 10px;
    font-family: "Delius", cursive; font-size: 30px; color: var(--purple);
  }
  .site-logo .dot { width: 26px; height: 26px; border-radius: 50%; background: var(--purple); }

  .store-badge { position: absolute; top: 102px; height: 26px; border-radius: 3px; }
  .store-badge.dark { left: 860px; width: 89px; background: #222; }
  .store-badge.green { left: 953px; width: 77px; background: var(--green); }

  .main-nav {
    position: absolute; left: 164px; top: 138px; width: 866px; height: 67px;
    background: linear-gradient(var(--purple), var(--purple-dark));
    display: flex; align-items: center; padding: 0 0 0 30px;
  }
  .main-nav::before, .main-nav::after {
    content: ""; position: absolute; left: 0; right: 0;
    border-top: 1px dashed rgba(255,255,255,0.45);
  }
  .main-nav::before { top: 3px; }
  .main-nav::after { bottom: 3px; }
  .main-nav .menu { display: flex; gap: 24px; list-style: none; }
  .main-nav .menu a { font-family: "Delius", cursive; font-size: 17px; color: var(--white); }
  .social { position: absolute; right: 14px; top: 0; height: 100%; display: flex; align-items: center; gap: 12px; list-style: none; }
  .social a { display: flex; align-items: center; gap: 5px; font-family: "Delius", cursive; font-size: 13px; color: var(--white); }
  .social .ring { width: 14px; height: 14px; border-radius: 50%; background: var(--white); }

  .feature {
    position: absolute; left: 164px; top: 205px; width: 865px; height: 374px;
    background: var(--white); box-shadow: 0 2px 6px rgba(0,0,0,0.08);
  }
  .feature-video {
    position: absolute; left: 33px; top: 61px; width: 485px; height: 272px;
    background: radial-gradient(ellipse at 50% 45%, #c9a96b 0%, #8a6a3c 45%, #111 75%);
  }
  .feature-copy { position: absolute; left: 549px; top: 64px; width: 290px; }
  .feature-copy h1 { font-family: "Delius", cursive; font-weight: 400; font-size: 23px; color: var(--purple-text); margin-bottom: 10px; }
  .feature-copy p { font-size: 13px; line-height: 27.7px; color: var(--body); }
  .app-button {
    position: absolute; left: 548px; top: 281px; width: 261px; height: 53px;
    background: var(--green); border-bottom: 3px solid var(--green-dark);
    display: flex; align-items: center; justify-content: space-between; padding: 0 10px 0 17px;
    font-family: "Delius", cursive; font-size: 19px; color: var(--white);
  }

  .character { position: absolute; }
  .character.left { left: 0; top: 328px; width: 164px; height: 272px;
    background: linear-gradient(#f2c25a, #e9483e 70%, #c8884f); border-radius: 40px 40px 10px 10px; }
  .character.right { left: 1029px; top: 314px; width: 141px; height: 291px;
    background: linear-gradient(#f4d7b0 0%, #ef6a36 35%, #7f5fb0 75%, #6b4ea6); border-radius: 40px 40px 10px 10px; }

  .commercials-title { position: absolute; left: 0; width: 1200px; top: 618px; text-align: center;
    font-family: "Delius", cursive; font-size: 18px; font-weight: 400; color: var(--ink); }
  .advert { position: absolute; top: 666px; width: 290px; }
  .advert-thumb { width: 276px; height: 155px; }
  .advert h2 { font-family: "Delius", cursive; font-weight: 400; font-size: 18px; color: var(--ink); margin: 10px 0 4px; }
  .advert p { font-size: 12.4px; line-height: 27.7px; color: var(--body); }
  .read-more { display: inline-block; margin-top: 7px; width: 97px; height: 34px; line-height: 34px; text-align: center;
    background: var(--green); font-family: "Delius", cursive; font-size: 15px; color: var(--white); }

  .site-footer { position: absolute; left: 0; width: 1200px; top: 1053px; text-align: center;
    font-family: "Delius", cursive; font-size: 15px; color: var(--ink); line-height: 28px; }
  .guild-mark { position: absolute; left: 940px; top: 1060px; width: 110px;
    display: flex; align-items: center; gap: 5px; font-family: "Delius", cursive; font-size: 10px; line-height: 12px; color: var(--ink); }
  .guild-mark .square { width: 14px; height: 14px; background: #b22b22; flex: none; }
</style>
</head>
<body>
  <a class="site-logo" href="#"><span class="dot"></span>Skip Along Today</a>
  <a class="store-badge dark" href="#" aria-label="App download listing"></a>
  <a class="store-badge green" href="#" aria-label="Second app download listing"></a>

  <nav class="main-nav">
    <ul class="menu">
      <li><a href="#">Play Right Now</a></li>
      <li><a href="#">Get Involved</a></li>
      <li><a href="#">Why Play</a></li>
      <li><a href="#">Fun Forever</a></li>
      <li><a href="#">Resources</a></li>
    </ul>
    <ul class="social">
      <li><a href="#"><span class="ring"></span>Vidbox</a></li>
      <li><a href="#"><span class="ring"></span>Peepsy</a></li>
      <li><a href="#"><span class="ring"></span>Chatterly</a></li>
    </ul>
  </nav>

  <div class="character left" role="img" aria-label="Illustrated boy character in a checked shirt and red shorts"></div>
  <div class="character right" role="img" aria-label="Illustrated boy character in an orange jumper and striped shorts"></div>

  <section class="feature">
    <div class="feature-video" role="img" aria-label="Video player showing the Skip Along Today advert"></div>
    <div class="feature-copy">
      <h1>Skip Along Today Advert</h1>
      <p>Lorem Ipsum is simply dummy text of the printing and typesetting industry. Lorem Ipsum has been the industry's standard dummy text ever since the 1500s, when an unknown printer took a galley of type and scrambled it to make a type specimen book.</p>
    </div>
    <a class="app-button" href="#">Skip Along Today App
      <svg width="32" height="32" viewBox="0 0 32 32" aria-hidden="true"><circle cx="16" cy="16" r="16" fill="#fff"/><path d="M12 9 L23 16 L12 23 Z" fill="#a9c93a"/></svg>
    </a>
  </section>

  <h2 class="commercials-title">Our New Commercials</h2>

  <article class="advert" style="left:165px">
    <div class="advert-thumb" role="img" aria-label="Illustration of children playing under a tree" style="background:linear-gradient(#3f7a3a,#7aa24a 60%,#5d8c3c)"></div>
    <h2>Advert 1</h2>
    <p>Lorem Ipsum is simply dummy text of the<br>printing and typesetting industry. Lorem Ipsum<br>has been the industry's standard dummy</p>
    <a class="read-more" href="#">Read More</a>
  </article>
  <article class="advert" style="left:463px">
    <div class="advert-thumb" role="img" aria-label="Illustration of children playing fair on a chequered floor" style="background:linear-gradient(135deg,#3fa6c4,#e6c23a 55%,#3f9ab4)"></div>
    <h2>Advert 2</h2>
    <p>Lorem Ipsum is simply dummy text of the<br>printing and typesetting industry. Lorem Ipsum<br>has been the industry's standard dummy</p>
    <a class="read-more" href="#">Read More</a>
  </article>
  <article class="advert" style="left:755px">
    <div class="advert-thumb" role="img" aria-label="Illustration of a child facing a green dragon in a classroom" style="background:linear-gradient(#8fb3c8,#7ea6bd)"></div>
    <h2>Advert 3</h2>
    <p>Lorem Ipsum is simply dummy text of the<br>printing and typesetting industry. Lorem Ipsum<br>has been the industry's standard dummy</p>
    <a class="read-more" href="#">Read More</a>
  </article>

  <footer class="site-footer">
    <p>© 2010 Northfield Games &amp; Pastimes Guild Ltd. All Rights Reserved</p>
    <p>14 Larkspur Lane, Leeds, LS7 2QB &nbsp;&nbsp;| Disclaimer</p>
  </footer>
  <div class="guild-mark"><span class="square"></span>Northfield Games &amp; Pastimes Guild</div>
</body>
</html>
```